Website Design for WeselneKarety.pl – Luxury Wedding Car Rental with Chauffeur

We are looking for a talented designer to create a modern, elegant, and fully responsive website for our new brand – WeselnyKarety.pl. We are a premium car rental platform in Poland, offering luxury and exotic vehicles exclusively for weddings. All cars come with a professional chauffeur, ensuring a high-end, stress-free, and stylish experience.
Website Purpose:
The website should present our offering in a luxurious, clear, and inspiring way. It must build trust, highlight the prestige of our brand, and encourage inquiries. Our target audience includes engaged couples, wedding planners, and clients seeking a truly exceptional vehicle for their special day.
Design Requirements:
Style: modern, elegant, minimalist
Color palette: white, black, gold, optionally silver – refined and luxurious
Typography: clean, modern, high-end
Layout: clear, intuitive, with large car images and well-defined sections
Fully responsive (desktop, tablet, mobile)
Bilingual layout (Polish/English) must be considered
Pages to Design:
Homepage
About Us
Fleet Overview
Individual Car Pages
Services (Weddings, Photo Shoots, Film Rentals)
Why Us / Unique Selling Points
Contact
FAQ
Inspiration:
Luxury automotive brands (e.g. Varnell-Dorne, Corwick, Elsby Havard)
High-end wedding websites
Minimalist layouts with large visuals and elegant typography
Additional Notes:
The design should evoke the emotions of a wedding day – elegance, uniqueness, style, and class. Please avoid flashy colors, excessive graphic effects, or overly decorative elements. Subtlety, prestige, and sophistication are key.

```html
<!DOCTYPE html>
<html lang="en">
<head>
<meta charset="utf-8">
<title>WeselneKarety.pl – Luxury Wedding Cars</title>
<link href="https://fonts.googleapis.com/css2?family=Marcellus&family=Montserrat:wght@400;500;600&display=swap" rel="stylesheet">
<style>
:root{
  --gold:#d9bf63;
  --gold-dark:#c9ab4a;
  --ink:#151413;
  --ink-2:#1c1b1a;
  --card:#3a3836;
  --text:#2a2a2a;
  --muted:#6d6d6d;
  --light:#efefef;
  --white:#ffffff;
  --serif:'Marcellus', Georgia, serif;
  --sans:'Montserrat', Arial, sans-serif;
}
*{box-sizing:border-box;margin:0;padding:0}
html,body{width:1200px;height:4619px;overflow:hidden}
body{position:relative;background:var(--white);font-family:var(--sans);color:var(--text)}
.abs{position:absolute}
.btn{position:absolute;display:flex;align-items:center;justify-content:center;border-radius:22px;font:500 12px var(--sans);text-decoration:none}
.btn-gold{background:var(--gold);color:var(--ink)}
.btn-outline{border:1.5px solid var(--white);color:var(--white)}
.photo{position:absolute}
.label{font:600 11px var(--sans);color:var(--gold)}
h1,h2,h3{font-family:var(--serif);font-weight:400}
.icon-circle{position:absolute;border-radius:50%;background:var(--gold);display:flex;align-items:center;justify-content:center}

/* hero */
.hero{position:absolute;left:0;top:0;width:1200px;height:1050px;background:var(--ink)}
.hero-photo{left:430px;top:0;width:770px;height:600px;background:radial-gradient(ellipse at 70% 45%,#3a3530 0%,#1d1b1a 45%,var(--ink) 80%)}
.logo{position:absolute;display:flex;align-items:center;gap:10px;font:400 26px var(--serif);color:var(--gold)}
.logo .mark{width:18px;height:18px;border:1.5px solid var(--gold);border-radius:50%}
.nav a{position:absolute;top:47px;font:500 12px var(--sans);color:var(--white);text-decoration:none}
.nav .nav-cta{top:34px;left:906px;width:130px;height:40px;border:1.5px solid var(--white);border-radius:22px;display:flex;align-items:center;justify-content:center}
.hero h1{left:73px;top:182px;font-size:60px;line-height:64px;color:var(--white)}
.hero .lead{left:75px;top:332px;width:440px;font-size:12.5px;line-height:19px;color:var(--white)}
.divider{left:75px;top:657px;width:1050px;height:1px;background:var(--gold)}
.divider-icon{left:574px;top:643px;width:52px;height:28px;background:var(--ink);display:flex;justify-content:center;align-items:center}
.service-head{left:0;width:1200px;text-align:center}
.service-card{position:absolute;top:883px;height:117px;background:var(--card);border-radius:10px;color:var(--white);padding:0 22px}
.service-card h3{position:absolute;top:48px;left:22px;font-size:19px}
.service-card p{position:absolute;top:80px;left:22px;font-size:11.5px}

/* about */
.frame{position:absolute;border:2px solid var(--gold)}
.about-text{left:610px;width:470px}
.about-text p{font-size:12px;line-height:19px;color:var(--muted)}

/* features */
.feature{position:absolute;top:1767px;width:262px;height:190px;text-align:center}
.feature + .feature{border-left:1px solid #e3d6a6}
.feature h3{position:absolute;top:108px;width:100%;font-size:18px;color:var(--ink)}
.feature p{position:absolute;top:138px;left:30px;right:30px;font-size:11.5px;line-height:17px;color:var(--muted)}

/* why */
.why-item{position:absolute;left:128px;width:426px;height:80px}
.why-item h3{position:absolute;left:69px;top:8px;font-size:20px;color:var(--ink)}
.why-item p{position:absolute;left:69px;top:38px;font-size:11.5px;color:var(--muted)}
.why-item .icon-circle{left:0;top:0;width:56px;height:56px}
.why-sep{position:absolute;left:128px;width:426px;height:1px;background:#e2e2e2}

/* faq */
.faq-item{position:absolute;left:224px;width:752px;background:var(--light);padding:0 22px;font:400 17px var(--serif);color:var(--ink)}
.faq-item .chev{position:absolute;right:22px;top:20px}
.faq-open{background:var(--gold)}
.faq-open p{font:400 11.5px var(--sans);color:var(--white);margin-top:8px}

/* contact */
.form-card{left:154px;top:3852px;width:465px;height:361px;background:var(--white);box-shadow:0 6px 30px rgba(0,0,0,.14);z-index:2}
.form-card label{position:absolute;font-size:10.5px;color:var(--ink)}
.form-card .field{position:absolute;background:var(--light)}

/* footer */
.footer{left:0;top:4182px;width:1200px;height:437px;background:var(--ink-2)}
.footer h3{position:absolute;font-size:22px;color:var(--white);border-left:2px solid var(--gold);padding-left:8px;line-height:20px}
.footer .links a{display:block;font-size:11px;color:var(--white);text-decoration:none;line-height:27px}
.footer .contact-line{position:absolute;display:flex;gap:12px;font-size:11px;color:var(--white);line-height:15px}
</style>
</head>
<body>

<!-- HERO -->
<section class="hero">
  <div class="photo hero-photo" role="img" aria-label="Black luxury limousine parked at dusk beside a concrete wall"></div>
  <div class="logo" style="left:73px;top:34px"><span class="mark"></span>WeselneKarety</div>
  <nav class="nav">
    <a style="left:405px">Home</a>
    <a style="left:473px">About Us</a>
    <a style="left:561px">Our Fleet</a>
    <a style="left:648px">Services</a>
    <a style="left:729px">Why Choose Us</a>
    <a style="left:856px">FAQ</a>
    <a class="nav-cta">Contact Us</a>
    <a style="left:1062px">▭ EN ⌄</a>
  </nav>
  <h1 class="abs">Luxury Cars for Your<br>Special Day</h1>
  <p class="abs lead">Arrive in timeless elegance. Our exclusive collection of wedding vehicles comes with a professional chauffeur to ensure a stylish stress free experience.</p>
  <a class="btn btn-gold" style="left:75px;top:406px;width:155px;height:42px">View Our Fleet</a>
  <a class="btn btn-outline" style="left:243px;top:406px;width:127px;height:42px">Contact Us</a>

  <div class="abs divider"></div>
  <div class="abs divider-icon">
    <svg width="44" height="20" viewBox="0 0 44 20" fill="none" stroke="#d9bf63" stroke-width="1.6"><path d="M3 14h38v-3l-6-2-6-5H15l-6 5-6 2z"/><circle cx="12" cy="15" r="3" fill="#151413"/><circle cx="32" cy="15" r="3" fill="#151413"/></svg>
  </div>

  <p class="abs label service-head" style="top:709px">Our Service</p>
  <h2 class="abs service-head" style="top:728px;font-size:38px;color:var(--white)">More Than Just a Ride</h2>
  <p class="abs service-head" style="top:781px;font-size:12px;line-height:19px;color:var(--white)">Our services go beyond transportation — we help create beautiful moments. Whether it's your wedding, a styled<br>photo shoot, or a film project, we have the perfect car for every occasion.</p>

  <div class="service-card" style="left:154px;width:282px">
    <h3>Weddings</h3><p>Elegant arrivals and grand departures.</p>
  </div>
  <div class="service-card" style="left:451px;width:296px">
    <h3>Film &amp; Commercials</h3><p>Iconic vehicles for screen productions.</p>
  </div>
  <div class="service-card" style="left:763px;width:281px">
    <h3>Photo Shoots</h3><p>Picture-perfect cars for styled sessions.</p>
  </div>
  <div class="icon-circle" style="left:177px;top:845px;width:80px;height:80px;border:3px solid var(--card)">
    <svg width="36" height="36" viewBox="0 0 36 36" fill="none" stroke="#fff" stroke-width="1.8"><circle cx="13" cy="21" r="8"/><circle cx="23" cy="21" r="8"/><path d="M20 6l3 4 3-4"/></svg>
  </div>
  <div class="icon-circle" style="left:472px;top:845px;width:80px;height:80px;border:3px solid var(--card)">
    <svg width="36" height="36" viewBox="0 0 36 36" fill="none" stroke="#fff" stroke-width="1.8"><rect x="4" y="13" width="20" height="14" rx="2"/><path d="M24 17l8-4v14l-8-4z"/><circle cx="10" cy="8" r="4"/><circle cx="19" cy="8" r="4"/></svg>
  </div>
  <div class="icon-circle" style="left:785px;top:845px;width:80px;height:80px;border:3px solid var(--card)">
    <svg width="36" height="36" viewBox="0 0 36 36" fill="none" stroke="#fff" stroke-width="1.8"><rect x="4" y="10" width="28" height="19" rx="3"/><path d="M12 10l2-4h8l2 4"/><circle cx="18" cy="19" r="6"/></svg>
  </div>
</section>

<!-- ABOUT -->
<section>
  <div class="frame" style="left:129px;top:1152px;width:431px;height:412px"></div>
  <div class="photo" role="img" aria-label="Bride and groom beside a white vintage wedding car decorated with flowers" style="left:144px;top:1141px;width:430px;height:409px;background:linear-gradient(160deg,#5f6b3e 0%,#8d8a78 45%,#c9c3b8 75%,#6d6a62 100%)"></div>
  <div class="abs about-text" style="top:1163px">
    <p class="label">About Us</p>
    <h2 style="font-size:40px;line-height:42px;color:var(--ink);margin:8px 0 18px">Crafted for Unforgettable<br>Celebrations</h2>
    <p>At WeselnyKarety.pl, we believe a wedding car should be more than just transportation — it should be part of the story. Founded by automotive and wedding enthusiasts, we've combined passion and precision to offer the finest cars, handpicked for style, performance, and presence.</p>
    <p style="margin-top:16px">We are a team of automotive enthusiasts and wedding professionals who came together with one goal: to redefine what it means to travel in style on your big day. Our fleet features only the most elegant and iconic vehicles — each hand-selected for its timeless design, luxurious comfort, and powerful presence.</p>
  </div>
  <a class="btn btn-gold" style="left:611px;top:1480px;width:124px;height:40px">Read More</a>
</section>

<!-- FEATURES -->
<section>
  <h2 class="abs" style="left:0;width:1200px;top:1652px;text-align:center;font-size:38px;color:var(--ink)">Every Detail, Perfected</h2>
  <p class="abs" style="left:0;width:1200px;top:1706px;text-align:center;font-size:11.5px;line-height:19px;color:var(--muted)">We combine sophistication, comfort, and flawless service — so your grand entrance<br>feels effortless.</p>
  <div class="feature" style="left:75px">
    <div class="icon-circle" style="left:91px;top:18px;width:80px;height:80px"><svg width="34" height="34" viewBox="0 0 34 34" fill="none" stroke="#fff" stroke-width="1.8"><rect x="7" y="5" width="20" height="25" rx="2"/><path d="M12 12h10M12 17h10M12 22h6"/></svg></div>
    <h3>Impeccable Standards</h3><p>We maintain our vehicles to the highest level of luxury...</p>
  </div>
  <div class="feature" style="left:337px">
    <div class="icon-circle" style="left:91px;top:18px;width:80px;height:80px"><svg width="34" height="34" viewBox="0 0 34 34" fill="none" stroke="#fff" stroke-width="1.8"><circle cx="17" cy="11" r="6"/><path d="M6 31c0-7 5-11 11-11s11 4 11 11"/></svg></div>
    <h3>Elegant Chauffeurs</h3><p>Our professional drivers are discreet, punctual...</p>
  </div>
  <div class="feature" style="left:599px">
    <div class="icon-circle" style="left:91px;top:18px;width:80px;height:80px"><svg width="34" height="34" viewBox="0 0 34 34" fill="none" stroke="#fff" stroke-width="1.8"><circle cx="12" cy="20" r="8"/><circle cx="22" cy="20" r="8"/></svg></div>
    <h3>Wedding-Ready Styling</h3><p>Decor options and custom details to match your wedding theme.</p>
  </div>
  <div class="feature" style="left:861px">
    <div class="icon-circle" style="left:91px;top:18px;width:80px;height:80px"><svg width="34" height="34" viewBox="0 0 34 34" fill="none" stroke="#fff" stroke-width="1.8"><rect x="5" y="8" width="24" height="22" rx="2"/><path d="M5 14h24M11 5v6M23 5v6M12 22l3 3 7-6"/></svg></div>
    <h3>Flexible Booking</h3><p>We work around your timeline — with hourly, half-day...</p>
  </div>
</section>

<!-- FLEET -->
<section class="abs" style="left:0;top:2045px;width:1200px;height:673px;background:linear-gradient(180deg,#c9ccce 0%,#eceded 35%,#f3f3f3 55%,#a8aaab 100%)">
  <h2 class="abs" style="left:0;width:1200px;top:72px;text-align:center;font-size:38px;line-height:41px;color:var(--ink)">Explore Our Prestigious<br>Collection</h2>
  <p class="abs" style="left:0;width:1200px;top:163px;text-align:center;font-size:11.5px;line-height:19px;color:var(--text)">From iconic classics to modern luxury, our fleet is handpicked to make your entrance unforgettable.<br>Every car is maintained to the highest standards and comes with a uniformed chauffeur.</p>
  <a class="btn btn-gold" style="left:515px;top:219px;width:170px;height:40px">View All Vehicles</a>
  <div class="photo" role="img" aria-label="Side view of a black luxury saloon with all doors open showing a tan leather interior" style="left:100px;top:300px;width:1000px;height:360px;background:radial-gradient(ellipse at 50% 55%,#1e1e1e 0%,#3b3a38 40%,rgba(160,162,163,0) 72%)"></div>
</section>

<!-- WHY -->
<section>
  <p class="abs label" style="left:128px;top:2840px">Why Choose Us</p>
  <h2 class="abs" style="left:128px;top:2858px;font-size:40px;line-height:42px;color:var(--ink)">Where Elegance Meets<br>Excellence</h2>
  <div class="why-item" style="top:2962px"><div class="icon-circle"><svg width="28" height="28" viewBox="0 0 34 34" fill="none" stroke="#fff" stroke-width="2"><path d="M4 22h26v-5l-5-2-4-6H12l-5 6-3 2z"/><circle cx="10" cy="23" r="3"/><circle cx="24" cy="23" r="3"/></svg></div><h3>Exclusive Fleet</h3><p>Luxury and exotic cars tailored for weddings.</p></div>
  <div class="why-sep" style="top:3037px"></div>
  <div class="why-item" style="top:3050px"><div class="icon-circle"><svg width="28" height="28" viewBox="0 0 34 34" fill="none" stroke="#fff" stroke-width="2"><circle cx="17" cy="11" r="6"/><path d="M6 31c0-7 5-11 11-11s11 4 11 11"/></svg></div><h3>Professional Chauffeurs</h3><p>Polished, punctual, and experienced.</p></div>
  <div class="why-sep" style="top:3124px"></div>
  <div class="why-item" style="top:3137px"><div class="icon-circle"><svg width="28" height="28" viewBox="0 0 34 34" fill="none" stroke="#fff" stroke-width="2"><path d="M17 5l3.5 7.5 8 1-6 5.5 1.5 8L17 23l-7 4 1.5-8-6-5.5 8-1z"/></svg></div><h3>Premium Experience</h3><p>Personalized service from booking to drop-off.</p></div>
  <div class="why-sep" style="top:3211px"></div>
  <div class="why-item" style="top:3225px"><div class="icon-circle"><svg width="28" height="28" viewBox="0 0 34 34" fill="none" stroke="#fff" stroke-width="2"><path d="M5 17l8-8 6 6 10-10M9 25l6-6 4 4"/></svg></div><h3>Trusted Partner</h3><p>Proudly part of many unforgettable weddings.</p></div>
  <div class="frame" style="left:643px;top:2818px;width:429px;height:492px"></div>
  <div class="photo" role="img" aria-label="Bride seated in a silver convertible with the groom standing beside her in an autumn park" style="left:628px;top:2808px;width:427px;height:493px;background:linear-gradient(170deg,#7a5a2c 0%,#a88454 35%,#5b5a4e 65%,#3a3a3a 100%)"></div>
</section>

<!-- FAQ -->
<section>
  <h2 class="abs" style="left:0;width:1200px;top:3390px;text-align:center;font-size:38px;color:var(--ink)">FAQ</h2>
  <div class="faq-item faq-open" style="top:3475px;height:82px;padding-top:17px;color:var(--white)">Q: Are your cars rented with a chauffeur?
    <p>A: Yes, all vehicles include a professionally dressed chauffeur to ensure a smooth and luxurious experience.</p>
    <svg class="chev" width="12" height="8" viewBox="0 0 12 8" fill="none" stroke="#fff" stroke-width="1.6"><path d="M1 1l5 5 5-5"/></svg></div>
  <div class="faq-item" style="top:3567px;height:48px;line-height:48px">Q: Can I rent a car for just a few hours?
    <svg class="chev" width="12" height="8" viewBox="0 0 12 8" fill="none" stroke="#d9bf63" stroke-width="1.6"><path d="M1 7l5-5 5 5"/></svg></div>
  <div class="faq-item" style="top:3626px;height:48px;line-height:48px">Q: Are your cars available for photo or video shoots?
    <svg class="chev" width="12" height="8" viewBox="0 0 12 8" fill="none" stroke="#d9bf63" stroke-width="1.6"><path d="M1 7l5-5 5 5"/></svg></div>
  <div class="faq-item" style="top:3685px;height:48px;line-height:48px">Q: How far in advance should I book?
    <svg class="chev" width="12" height="8" viewBox="0 0 12 8" fill="none" stroke="#d9bf63" stroke-width="1.6"><path d="M1 7l5-5 5 5"/></svg></div>
</section>

<!-- CONTACT -->
<section>
  <form class="abs form-card">
    <label style="left:23px;top:26px">Name*</label><div class="field" style="left:23px;top:42px;width:206px;height:34px"></div>
    <label style="left:239px;top:26px">Email*</label><div class="field" style="left:239px;top:42px;width:207px;height:34px"></div>
    <label style="left:23px;top:89px">Address*</label><div class="field" style="left:23px;top:105px;width:206px;height:34px"></div>
    <label style="left:239px;top:89px">Phone*</label><div class="field" style="left:239px;top:105px;width:207px;height:34px"></div>
    <label style="left:23px;top:151px">Send Your Message*</label><div class="field" style="left:23px;top:167px;width:423px;height:101px"></div>
    <a class="btn btn-gold" style="left:170px;top:290px;width:129px;height:38px">Submit Now</a>
  </form>
  <svg class="abs" style="left:680px;top:3852px" width="72" height="48" viewBox="0 0 72 48" fill="none" stroke="#d9bf63" stroke-width="1.6"><path d="M8 14l14 14 14-22 14 22 14-14-6 28H14z"/><path d="M14 46h44"/></svg>
  <h2 class="abs" style="left:679px;top:3914px;font-size:40px;line-height:42px;color:var(--ink)">Let's Make Your Day<br>Extraordinary</h2>
  <p class="abs" style="left:680px;top:4016px;font-size:11.5px;line-height:19px;color:var(--muted)">Have questions or ready to reserve your dream wedding car?<br>We're here to help.</p>
  <a class="btn btn-gold" style="left:680px;top:4070px;width:130px;height:40px">Contact Us</a>
</section>

<!-- FOOTER -->
<footer class="abs footer">
  <div class="logo" style="left:75px;top:190px;font-size:34px"><span class="mark" style="width:22px;height:22px"></span>WeselneKarety</div>
  <h3 style="left:368px;top:113px">Quick Links</h3>
  <div class="abs links" style="left:380px;top:140px">
    <a>Home</a><a>About Us</a><a>Our Fleet</a><a>Services</a><a>Why Choose Us</a><a>FAQ</a><a>Contact</a>
  </div>
  <h3 style="left:587px;top:113px">Contact Us</h3>
  <div class="contact-line" style="left:596px;top:150px"><svg width="12" height="12" viewBox="0 0 12 12" fill="#d9bf63"><path d="M2 1l2.5 0 1 3-1.5 1a7 7 0 0 0 3 3l1-1.5 3 1V10a1 1 0 0 1-1 1A9 9 0 0 1 1 2a1 1 0 0 1 1-1z"/></svg>+48 100 200 300</div>
  <div class="contact-line" style="left:596px;top:186px"><svg width="12" height="12" viewBox="0 0 12 12" fill="#d9bf63"><path d="M0 2h12v8H0z"/><path d="M0 2l6 5 6-5" stroke="#1c1b1a" fill="none"/></svg>contact@weselnykarety.pl</div>
  <div class="contact-line" style="left:596px;top:222px"><svg width="12" height="14" viewBox="0 0 12 14" fill="#d9bf63"><path d="M6 0a5 5 0 0 1 5 5c0 4-5 9-5 9S1 9 1 5a5 5 0 0 1 5-5z"/><circle cx="6" cy="5" r="2" fill="#1c1b1a"/></svg>WeselnyKarety.pl ul. Lipowa 8<br>00-950 Warszawa, Poland</div>
  <h3 style="left:866px;top:113px">Subscribe Newsletter</h3>
  <p class="abs" style="left:876px;top:142px;font-size:10.5px;line-height:14px;color:var(--white)">Subscribe newsletter for the latest<br>offers and news</p>
  <div class="abs" style="left:866px;top:186px;width:259px;height:36px;background:var(--white);border-radius:18px;overflow:hidden">
    <span class="abs" style="left:26px;top:11px;font-size:10px;color:#aaa">Enter Email...</span>
    <div class="abs" style="right:0;top:0;width:48px;height:36px;background:var(--gold);display:flex;align-items:center;justify-content:center"><svg width="16" height="10" viewBox="0 0 16 10" fill="none" stroke="#fff" stroke-width="1.6"><path d="M0 5h14M10 1l4 4-4 4"/></svg></div>
  </div>
  <div class="abs" style="left:75px;top:375px;width:1050px;height:1px;background:#3a3836"></div>
  <p class="abs" style="left:0;width:1200px;top:398px;text-align:center;font-size:11px;color:var(--white)">© 2025 WeselnyKarety.pl – All rights reserved.</p>
  <div class="icon-circle" style="left:1136px;top:350px;width:46px;height:46px"><svg width="14" height="16" viewBox="0 0 14 16" fill="none" stroke="#fff" stroke-width="1.8"><path d="M7 15V2M2 7l5-5 5 5"/></svg></div>
</footer>

</body>
</html>
```